Visual consulting framework

Tamsworth Advisory is a financial consulting business that takes it clients on the following journey:
1. Get fit (disciplined)
2. Get funded (access to capital)
3. Get big (grow)
4. Get out (exit with wealth)
Over thirty years we have identified that the key to being successful on this journey are the following elements or components.
1. Vision
2. Strategy
3. Structure
4. Product & services
5. Sales and marketing
6. System and processes
7. People
8. Culture
9. Finance
10. M&A
11. Performance monitoring
12. Risk management
We require a visual representation of these elements and the journey to communicate to clients and prospects in marketing material.

```html
<!DOCTYPE html>
<html lang="en">
<head>
<meta charset="utf-8">
<title>Tamsworth Advisory – Consulting Framework</title>
<link rel="stylesheet" href="https://fonts.googleapis.com/css2?family=Bebas+Neue&family=Montserrat:wght@700&display=swap">
<style>
  :root {
    --orange: #f7941d;
    --blue: #00a6e8;
    --ink: #2b2b2b;
    --paper: #ffffff;
    --backdrop: #ececec;
    --icon-well: #f1f1f1;
    --dot: #c9c9c9;
  }
  html, body {
    margin: 0;
    width: 800px;
    height: 1200px;
    overflow: hidden;
    background: var(--backdrop);
  }
  .framework-card {
    position: absolute;
    left: 20px;
    top: 306px;
    width: 760px;
    height: 587px;
    display: block;
  }
  .headline { font-family: "Bebas Neue", Impact, sans-serif; font-size: 50px; fill: var(--paper); }
  .center-title { font-family: "Bebas Neue", Impact, sans-serif; font-size: 50px; fill: var(--ink); }
  .element-label { font-family: "Montserrat", Arial, sans-serif; font-weight: 700; font-size: 21px; fill: var(--paper); }
  .stage-label { font-family: "Montserrat", Arial, sans-serif; font-weight: 700; font-size: 23px; fill: var(--paper); letter-spacing: 1px; }
  .brand-name { font-family: "Montserrat", Arial, sans-serif; font-weight: 700; font-size: 24px; fill: var(--blue); }
  .fill-orange { fill: var(--orange); }
  .fill-blue { fill: var(--blue); }
  .stroke-orange { stroke: var(--orange); }
  .stroke-blue { stroke: var(--blue); }
  .pill-frame { fill: var(--paper); stroke-width: 3; }
  .icon-ring { fill: var(--paper); stroke-width: 4; }
  .icon-well { fill: var(--icon-well); }
  .rail { fill: none; stroke-width: 5; }
  .knob { fill: var(--paper); stroke-width: 4; }
  .dotted-ring { fill: none; stroke: var(--dot); stroke-width: 4; stroke-dasharray: 1 8; stroke-linecap: round; }
</style>
</head>
<body>
<svg class="framework-card" viewBox="0 0 1224 945" xmlns="http://www.w3.org/2000/svg" aria-label="Tamsworth Advisory consulting framework">
  <defs>
    <path id="arc-get-out" d="M508,506 A104,104 0 0 1 612,402"/>
    <path id="arc-get-fit" d="M612,402 A104,104 0 0 1 716,506"/>
    <path id="arc-get-big" d="M493,506 A119,119 0 0 0 612,625"/>
    <path id="arc-get-funded" d="M612,625 A119,119 0 0 0 731,506"/>
  </defs>

  <!-- card -->
  <rect x="0" y="0" width="1224" height="945" fill="var(--paper)"/>
  <rect x="0" y="0" width="175" height="15" class="fill-orange"/>
  <rect x="167" y="0" width="1057" height="15" class="fill-blue"/>
  <rect x="0" y="930" width="612" height="15" class="fill-orange"/>
  <rect x="612" y="930" width="612" height="15" class="fill-blue"/>

  <!-- purpose banner -->
  <path class="fill-blue" d="M167,0 L1050,0 L986,118 Q976,138 950,138 L274,138 Q248,138 238,118 Z"/>
  <text class="headline" x="612" y="64" text-anchor="middle">OUR PURPOSE IS CLEAR, WE GET COMPANIES</text>
  <text class="headline" x="612" y="106" text-anchor="middle">AND THEIR FOUNDERS, FIT, FUNDED, BIG AND OUT</text>

  <!-- left rail -->
  <g class="rail-left">
    <path class="rail stroke-orange" d="M430,228 H466 V340"/>
    <path class="rail stroke-blue" d="M430,340 H466 V452"/>
    <path class="rail stroke-orange" d="M430,452 H466 V564"/>
    <path class="rail stroke-blue" d="M430,564 H466 V676"/>
    <path class="rail stroke-orange" d="M430,676 H466 V788"/>
    <path class="rail stroke-blue" d="M430,788 H466"/>
    <path class="rail stroke-blue" d="M466,506 H500"/>
    <circle class="knob stroke-orange" cx="458" cy="228" r="8"/>
    <circle class="knob stroke-blue" cx="458" cy="340" r="8"/>
    <circle class="knob stroke-orange" cx="458" cy="452" r="8"/>
    <circle class="knob stroke-blue" cx="458" cy="564" r="8"/>
    <circle class="knob stroke-orange" cx="458" cy="676" r="8"/>
    <circle class="knob stroke-blue" cx="458" cy="788" r="8"/>
  </g>

  <!-- right rail -->
  <g class="rail-right">
    <path class="rail stroke-orange" d="M794,228 H758 V340"/>
    <path class="rail stroke-blue" d="M794,340 H758 V452"/>
    <path class="rail stroke-orange" d="M794,452 H758 V564"/>
    <path class="rail stroke-blue" d="M794,564 H758 V676"/>
    <path class="rail stroke-orange" d="M794,676 H758 V788"/>
    <path class="rail stroke-blue" d="M794,788 H758"/>
    <path class="rail stroke-orange" d="M758,506 H724"/>
    <circle class="knob stroke-orange" cx="766" cy="228" r="8"/>
    <circle class="knob stroke-blue" cx="766" cy="340" r="8"/>
    <circle class="knob stroke-orange" cx="766" cy="452" r="8"/>
    <circle class="knob stroke-blue" cx="766" cy="564" r="8"/>
    <circle class="knob stroke-orange" cx="766" cy="676" r="8"/>
    <circle class="knob stroke-blue" cx="766" cy="788" r="8"/>
  </g>

  <!-- left elements -->
  <g class="element element-left">
    <rect class="pill-frame stroke-orange" x="82" y="179" width="348" height="98" rx="49"/>
    <rect class="fill-orange" x="90" y="187" width="320" height="82" rx="41"/>
    <circle class="icon-ring stroke-orange" cx="384" cy="228" r="46"/>
    <circle class="icon-well" cx="384" cy="228" r="37" role="img" aria-label="Vision icon: target with arrow"/>
    <text class="element-label" x="307" y="236" text-anchor="end">VISION</text>
  </g>
  <g class="element element-left">
    <rect class="pill-frame stroke-blue" x="82" y="291" width="348" height="98" rx="49"/>
    <rect class="fill-blue" x="90" y="299" width="320" height="82" rx="41"/>
    <circle class="icon-ring stroke-blue" cx="384" cy="340" r="46"/>
    <circle class="icon-well" cx="384" cy="340" r="37" role="img" aria-label="Strategy icon: planning board"/>
    <text class="element-label" x="307" y="348" text-anchor="end">STRATEGY</text>
  </g>
  <g class="element element-left">
    <rect class="pill-frame stroke-orange" x="82" y="403" width="348" height="98" rx="49"/>
    <rect class="fill-orange" x="90" y="411" width="320" height="82" rx="41"/>
    <circle class="icon-ring stroke-orange" cx="384" cy="452" r="46"/>
    <circle class="icon-well" cx="384" cy="452" r="37" role="img" aria-label="Structure icon: organisation chart"/>
    <text class="element-label" x="307" y="460" text-anchor="end">STRUCTURE</text>
  </g>
  <g class="element element-left">
    <rect class="pill-frame stroke-blue" x="82" y="515" width="348" height="98" rx="49"/>
    <rect class="fill-blue" x="90" y="523" width="320" height="82" rx="41"/>
    <circle class="icon-ring stroke-blue" cx="384" cy="564" r="46"/>
    <circle class="icon-well" cx="384" cy="564" r="37" role="img" aria-label="Product and services icon: hand holding a box"/>
    <text class="element-label" x="307" y="560" text-anchor="end">PRODUCT &amp;</text>
    <text class="element-label" x="307" y="582" text-anchor="end">SERVICES</text>
  </g>
  <g class="element element-left">
    <rect class="pill-frame stroke-orange" x="82" y="627" width="348" height="98" rx="49"/>
    <rect class="fill-orange" x="90" y="635" width="320" height="82" rx="41"/>
    <circle class="icon-ring stroke-orange" cx="384" cy="676" r="46"/>
    <circle class="icon-well" cx="384" cy="676" r="37" role="img" aria-label="Sales and marketing icon: hand with rising chart"/>
    <text class="element-label" x="307" y="672" text-anchor="end">SALES &amp;</text>
    <text class="element-label" x="307" y="694" text-anchor="end">MARKETING</text>
  </g>
  <g class="element element-left">
    <rect class="pill-frame stroke-blue" x="82" y="739" width="348" height="98" rx="49"/>
    <rect class="fill-blue" x="90" y="747" width="320" height="82" rx="41"/>
    <circle class="icon-ring stroke-blue" cx="384" cy="788" r="46"/>
    <circle class="icon-well" cx="384" cy="788" r="37" role="img" aria-label="Systems and processes icon: gear with cycle arrows"/>
    <text class="element-label" x="307" y="784" text-anchor="end">SYSTEM &amp;</text>
    <text class="element-label" x="307" y="806" text-anchor="end">PROCESSES</text>
  </g>

  <!-- right elements -->
  <g class="element element-right">
    <rect class="pill-frame stroke-orange" x="794" y="179" width="348" height="98" rx="49"/>
    <rect class="fill-orange" x="814" y="187" width="320" height="82" rx="41"/>
    <circle class="icon-ring stroke-orange" cx="840" cy="228" r="46"/>
    <circle class="icon-well" cx="840" cy="228" r="37" role="img" aria-label="People icon: group of people"/>
    <text class="element-label" x="921" y="236">PEOPLE</text>
  </g>
  <g class="element element-right">
    <rect class="pill-frame stroke-blue" x="794" y="291" width="348" height="98" rx="49"/>
    <rect class="fill-blue" x="814" y="299" width="320" height="82" rx="41"/>
    <circle class="icon-ring stroke-blue" cx="840" cy="340" r="46"/>
    <circle class="icon-well" cx="840" cy="340" r="37" role="img" aria-label="Culture icon: puzzle pieces"/>
    <text class="element-label" x="921" y="348">CULTURE</text>
  </g>
  <g class="element element-right">
    <rect class="pill-frame stroke-orange" x="794" y="403" width="348" height="98" rx="49"/>
    <rect class="fill-orange" x="814" y="411" width="320" height="82" rx="41"/>
    <circle class="icon-ring stroke-orange" cx="840" cy="452" r="46"/>
    <circle class="icon-well" cx="840" cy="452" r="37" role="img" aria-label="Finance icon: coin stack with dollar"/>
    <text class="element-label" x="921" y="460">FINANCE</text>
  </g>
  <g class="element element-right">
    <rect class="pill-frame stroke-blue" x="794" y="515" width="348" height="98" rx="49"/>
    <rect class="fill-blue" x="814" y="523" width="320" height="82" rx="41"/>
    <circle class="icon-ring stroke-blue" cx="840" cy="564" r="46"/>
    <circle class="icon-well" cx="840" cy="564" r="37" role="img" aria-label="M&amp;A icon: merger badge"/>
    <text class="element-label" x="921" y="572">M&amp;A</text>
  </g>
  <g class="element element-right">
    <rect class="pill-frame stroke-orange" x="794" y="627" width="348" height="98" rx="49"/>
    <rect class="fill-orange" x="814" y="635" width="320" height="82" rx="41"/>
    <circle class="icon-ring stroke-orange" cx="840" cy="676" r="46"/>
    <circle class="icon-well" cx="840" cy="676" r="37" role="img" aria-label="Performance monitoring icon: chart on screen"/>
    <text class="element-label" x="921" y="672">PERFORMANCE</text>
    <text class="element-label" x="921" y="694">MONITORING</text>
  </g>
  <g class="element element-right">
    <rect class="pill-frame stroke-blue" x="794" y="739" width="348" height="98" rx="49"/>
    <rect class="fill-blue" x="814" y="747" width="320" height="82" rx="41"/>
    <circle class="icon-ring stroke-blue" cx="840" cy="788" r="46"/>
    <circle class="icon-well" cx="840" cy="788" r="37" role="img" aria-label="Risk management icon: checklist with warning sign"/>
    <text class="element-label" x="921" y="784">RISK</text>
    <text class="element-label" x="921" y="806">MANAGEMENT</text>
  </g>

  <!-- journey wheel -->
  <g class="journey-wheel">
    <circle class="dotted-ring" cx="612" cy="506" r="162"/>
    <path class="fill-orange" d="M472,506 A140,140 0 0 1 752,506 Z"/>
    <path class="fill-blue" d="M472,506 A140,140 0 0 0 752,506 Z"/>
    <line x1="612" y1="366" x2="612" y2="646" stroke="var(--paper)" stroke-width="3"/>
    <line x1="472" y1="506" x2="752" y2="506" stroke="var(--paper)" stroke-width="3"/>
    <circle cx="612" cy="506" r="82" fill="var(--paper)"/>
    <text class="stage-label"><textPath href="#arc-get-out" startOffset="50%" text-anchor="middle">GET OUT</textPath></text>
    <text class="stage-label"><textPath href="#arc-get-fit" startOffset="50%" text-anchor="middle">GET FIT</textPath></text>
    <text class="stage-label"><textPath href="#arc-get-big" startOffset="50%" text-anchor="middle">GET BIG</textPath></text>
    <text class="stage-label"><textPath href="#arc-get-funded" startOffset="50%" text-anchor="middle">GET FUNDED</textPath></text>
    <text class="center-title" x="612" y="503" text-anchor="middle">MARKET</text>
    <text class="center-title" x="612" y="546" text-anchor="middle">LEADER</text>
  </g>

  <!-- brand -->
  <g class="brand">
    <circle cx="520" cy="864" r="26" class="fill-orange"/>
    <text class="brand-name" x="560" y="858">TAMSWORTH</text>
    <text class="brand-name" x="560" y="886">ADVISORY</text>
  </g>
</svg>
</body>
</html>
```